7 Vex Label

Design a label for 7 Vex styling gels. The logo is attached. The color is C=100, M=100, Y=0, K=0. The 16 oz. jar is also attached.

Updates

Attention all designers,

The old logo has been deleted.  I have uploaded a new logo for this project.  Can you please update your design with the NEW LOGO?
thank you,
Rob

Target Market(s)

Multicultural

Requirements
Must have
• you must used the logo attached.

text to be included on the jar:

Used by Professionals
Maximum Hold
Alcohol Free
NO FLAKING

16 oz.

As far as label size, use the jar photo, and fit the design on it.

```html
<!DOCTYPE html>
<html lang="en">
<head>
<meta charset="utf-8">
<title>7 Vex Styling Gel Label</title>
<link rel="stylesheet" href="https://fonts.googleapis.com/css2?family=Courier+Prime:wght@700&family=Tinos&display=swap">
<style>
  :root {
    --brand-blue: #2e3192;
    --deep-indigo: #1b1f6e;
    --royal-blue: #3a4fc4;
    --cyan: #1fb4e6;
    --sky: #8fd3f0;
    --ice: #dff1fb;
    --paper: #ffffff;
    --ink: #1a1a2e;
  }
  html, body {
    margin: 0;
    padding: 0;
    width: 1020px;
    height: 1200px;
    overflow: hidden;
    background: var(--paper);
  }
  .label {
    position: relative;
    width: 1020px;
    height: 1200px;
    background: var(--paper);
    overflow: hidden;
  }
  .artwork {
    position: absolute;
    left: 0;
    top: 0;
    width: 1020px;
    height: 1200px;
    display: block;
  }
  .logo {
    position: absolute;
    left: 200px;
    top: 380px;
    width: 360px;
    height: 190px;
    display: flex;
    align-items: center;
    justify-content: center;
  }
  .logo__name {
    font-family: "Courier Prime", "Courier New", monospace;
    font-weight: 700;
    font-size: 120px;
    line-height: 1;
    color: var(--brand-blue);
  }
  .claims {
    position: absolute;
    left: 560px;
    top: 672px;
    width: 420px;
    margin: 0;
    padding: 0;
    list-style: none;
    text-align: center;
    font-family: "Courier Prime", "Courier New", monospace;
    font-weight: 700;
    font-size: 36px;
    line-height: 46px;
    color: var(--paper);
  }
  .net-weight {
    position: absolute;
    left: 380px;
    top: 960px;
    width: 280px;
    margin: 0;
    text-align: center;
    font-family: "Tinos", "Times New Roman", serif;
    font-size: 56px;
    line-height: 1;
    letter-spacing: 2px;
    color: var(--ink);
  }
</style>
</head>
<body>
<main class="label">
  <svg class="artwork" viewBox="0 0 1020 1200" role="img" aria-label="Abstract blue paint splashes, a blue hexagon mosaic on the left and a cyan splash behind the claims">
    <defs>
      <linearGradient id="splashTop" x1="0" y1="0" x2="1" y2="1">
        <stop offset="0" stop-color="#2e3192"/>
        <stop offset="0.5" stop-color="#3a4fc4"/>
        <stop offset="1" stop-color="#1fb4e6"/>
      </linearGradient>
      <linearGradient id="hexLeft" x1="0" y1="0" x2="1" y2="0">
        <stop offset="0" stop-color="#1b1f6e"/>
        <stop offset="0.55" stop-color="#3a4fc4"/>
        <stop offset="1" stop-color="#dff1fb"/>
      </linearGradient>
      <radialGradient id="cyanSplash" cx="0.5" cy="0.5" r="0.6">
        <stop offset="0" stop-color="#1fb4e6"/>
        <stop offset="1" stop-color="#1596c9"/>
      </radialGradient>
    </defs>
    <path d="M300 170 C420 120 560 200 640 150 C760 90 900 140 1000 200 C1020 320 960 420 860 460 C760 500 700 600 600 560 C560 470 600 360 560 330 C480 300 360 330 300 260 Z" fill="url(#splashTop)" opacity="0.9"/>
    <path d="M0 170 C90 150 200 190 250 260 C200 330 110 320 60 380 C30 410 10 420 0 420 Z" fill="#2e3192" opacity="0.85"/>
    <path d="M0 560 C120 540 240 590 360 570 C480 550 560 620 600 700 C560 800 470 860 360 900 C240 950 120 980 0 1000 Z" fill="url(#hexLeft)" opacity="0.9"/>
    <path d="M560 800 C540 700 640 610 780 605 C900 600 990 680 985 780 C980 880 880 900 780 905 C660 910 580 890 560 800 Z" fill="url(#cyanSplash)"/>
  </svg>

  <div class="logo">
    <span class="logo__name">7 Vex</span>
  </div>

  <ul class="claims">
    <li>Used by</li>
    <li>Professionals</li>
    <li>Maximum Hold</li>
    <li>Alcohol Free</li>
    <li>NO FLAKING</li>
  </ul>

  <p class="net-weight">16 OZ.</p>
</main>
</body>
</html>
```